UPDATED 7/7 - Start-up Swimming Pool Care/Service Company In Need of Website

We sincerely appreciate everyone's interest in our website design project. In all we had 65 designs submitted and were amazed by the creativity and quality presented. Unfortunately, as with all contests, there can only be one winner and the winning firm was selected at 12:00 ET 7/7/2017. We wish you all the best and look forward to potentially working with you on future projects. Thanks again for your time and interests. Tobin

Thanks for your interest in our project! Due to the overwhelming number of submissions received, additional submissions will not be accepted after close of business 7/4. Additionally, to minimize unnecessary additional work, we will begin reviewing all submissions received on 7/5, select the submission(s) that come closest to meeting our needs and work with the designer(s) selected to finalize their designs. Thanks again.

Thanks for the feedback!!

Based on feedback provided, we understand that the initial specifications required that the site be developed as dynamic versus static and, as such, the budget was insufficient. With this in mind, we have modified the specifications as follows:
1. Clean, simple, uncluttered site
2. 4-5 pages consisting of the following:
a. Home page
b. About us
c. Services provided
d. Contact us/request quote/request service
2. No people in pools/photos unless it involves cleaning i.e., vacuuming, netting, etc.

We are in need of a website to promote our business and the services provided to our customers. The site should be a simple 5 page design providing information about us, the services we provide, our service territory (Central Florida = Seminole and Orange Counties), the ability to request a service quote, the ability to schedule service, the ability to pay invoices, the ability to refer neighbors and friends, the ability to leave reviews and provide feedback, etc. We are a certified, licensed, and insured veteran minority owned and operated company with 10 years industry experience providing unparalleled commercial and residential pool and spa care in the central Florida area. While we are seeking something more impressive and concise, an example of the site would be http://bluekettlepoolcare.example/ OR http://www.marlowaquaworks.example/

Target Market(s)

Hotels, motels, apartment complexes, condominium associations, homeowners associations, and individual homeowners

Contact Information for Business Card

Logo, name, phone number, website, "Certified Licensed Insured", "Providing quality pool care to Central Florida"

Coding

Coded - Design and coding required

Number of Pages Required

5+ page

Requirements
Must have
• See description
Nice to have
• See description
Should not have
• See description

```html
<!DOCTYPE html>
<html lang="en">
<head>
<meta charset="utf-8">
<title>Sunline Pool Pros</title>
<link rel="stylesheet" href="https://fonts.googleapis.com/css2?family=Lato:wght@400;700;900&family=Open+Sans:wght@400;600&family=Roboto:wght@400;500&display=swap">
<style>
:root{
  --blue:#2f5f9c;
  --blue-deep:#244f88;
  --blue-band:#3a6aa6;
  --sky:#e7f1fb;
  --orange:#e8641e;
  --ink:#222;
  --grey:#444;
  --dark:#2f2f2f;
  --white:#fff;
}
*{box-sizing:border-box;margin:0;padding:0}
html,body{width:1200px;height:2866px;overflow:hidden;background:#fff}
body{font-family:"Open Sans",sans-serif;color:var(--ink)}
.page{position:relative;width:1200px;height:2866px;overflow:hidden;background:#fff}
.abs{position:absolute}

/* header */
.brand{left:98px;top:34px;display:flex;align-items:center;gap:10px}
.brand-dot{width:16px;height:16px;border-radius:50%;background:var(--blue)}
.brand-name{font-family:"Lato",sans-serif;font-weight:900;font-size:30px;color:var(--blue);letter-spacing:.5px}
.contact-top{top:24px;right:98px;display:flex;gap:40px;font-family:"Roboto",sans-serif;font-size:15px;color:var(--ink)}
.contact-top span{display:flex;align-items:center;gap:10px}
.ico{width:30px;height:30px;border-radius:50%;display:inline-flex;align-items:center;justify-content:center}
.ico.blue{background:var(--blue)} .ico.orange{background:var(--orange)}
.nav{top:86px;right:98px;display:flex;gap:47px;font-family:"Roboto",sans-serif;font-size:15.5px;font-weight:500}
.nav a{color:var(--ink);text-decoration:none}
.nav a.current{color:var(--orange)}

/* hero */
.hero{left:0;top:130px;width:1200px;height:540px}
.hero-photo{position:absolute;inset:0;background:linear-gradient(135deg,#3f8fc9 0%,#5fb0de 35%,#2f7fbd 70%,#4aa0d6 100%)}
.hero-title{left:100px;top:265px;font-family:"Lato",sans-serif;font-weight:700;font-size:50px;color:#fff;letter-spacing:2px}
.hero-text{left:100px;top:352px;width:440px;font-size:15.5px;line-height:1.6;color:#fff}
.hero-btn{left:100px;top:444px;width:129px;height:48px;border:2px solid #fff;color:#fff;font-family:"Roboto",sans-serif;font-size:15px;display:flex;align-items:center;justify-content:center}
.arrow{top:368px}
.hero-wave{left:0;top:590px;width:1200px;height:80px}

/* section titles */
.sec-title{left:0;width:1200px;text-align:center;font-family:"Lato",sans-serif;font-weight:700;font-size:28px;color:var(--blue)}
.sec-rule{left:559px;width:82px;height:2px;background:var(--blue)}

/* services */
.service{width:300px;text-align:center}
.service-icon{width:150px;height:150px;margin:0 auto;border-radius:50%;border:3px solid var(--blue);display:flex;align-items:center;justify-content:center}
.service-icon .core{width:134px;height:134px;border-radius:50%;background:var(--blue);display:flex;align-items:center;justify-content:center}
.service-icon.alt{border-color:var(--orange)}
.service-icon.alt .core{background:var(--orange)}
.service h3{margin-top:36px;font-family:"Roboto",sans-serif;font-weight:500;font-size:20px;color:var(--ink);letter-spacing:.5px}
.service h3.alt{color:var(--orange)}
.service p{margin-top:22px;font-size:13.5px;line-height:1.95;color:var(--grey)}
.service svg.swash{display:block;margin:26px auto 0}

/* welcome band */
.band{left:0;top:1225px;width:1200px;height:570px}
.band-bg{position:absolute;inset:0}
.welcome-photo{left:98px;top:1377px;width:398px;height:274px;border:4px solid #fff;background:linear-gradient(160deg,#6f9c6a 0%,#5fa8c8 45%,#2e86b8 75%,#8a7b68 100%)}
.welcome-title{left:532px;top:1366px;font-family:"Lato",sans-serif;font-weight:700;font-size:28px;color:#fff}
.welcome-rule{left:532px;top:1414px;width:220px;height:2px;background:#fff}
.welcome-text{left:532px;top:1436px;width:578px;font-size:12.6px;line-height:1.95;color:#eef3fa;text-align:justify}
.welcome-text p+p{margin-top:8px}
.btn-fill{height:38px;border-radius:19px;background:var(--orange);border:2px solid #fff;color:#fff;font-family:"Roboto",sans-serif;font-weight:500;font-size:15px;display:flex;align-items:center;justify-content:center}

/* blog */
.blog-bg{left:0;top:1770px;width:1200px;height:700px;background:var(--sky)}
.post{width:305px;text-align:center}
.post-photo{height:196px;border:3px solid #9ab8d6;border-radius:18px 18px 4px 4px}
.post h3{margin-top:38px;font-family:"Roboto",sans-serif;font-weight:500;font-size:19px}
.post p{margin-top:10px;font-size:12.5px;line-height:1.75;color:var(--grey)}
.post .btn{margin:18px auto 0;width:114px;height:38px;border-radius:19px;font-family:"Roboto",sans-serif;font-weight:500;font-size:14.5px;display:flex;align-items:center;justify-content:center}
.btn.solid{background:var(--orange);color:#fff}
.btn.line{border:2px solid var(--blue);color:var(--blue);background:#fff}

/* footer */
.footer{left:0;top:2400px;width:1200px;height:466px}
.foot-brand{left:98px;top:2520px;display:flex;align-items:center;gap:10px}
.foot-brand .brand-name{color:#ddd}
.foot-brand .brand-dot{background:#ddd}
.foot-h{font-family:"Roboto",sans-serif;font-weight:500;font-size:17px;color:#fff;letter-spacing:.5px}
.foot-rule{height:2px;background:#fff;width:104px}
.links{list-style:none;font-family:"Roboto",sans-serif;font-size:14.5px;color:#fff}
.links li{height:32px}
.contact-item{display:flex;gap:18px;color:#fff;font-family:"Roboto",sans-serif}
.contact-item .c-ico{width:38px;height:38px;border:2px solid #fff;border-radius:50%;display:flex;align-items:center;justify-content:center;flex:none}
.contact-item b{display:block;font-weight:500;font-size:15px;margin-bottom:4px}
.contact-item span{font-size:12.5px;line-height:1.6;color:#ddd}
.field{height:38px;border:1px solid #ccc;border-radius:3px;color:#fff;font-size:11.5px;padding-left:12px;display:flex;align-items:center;font-family:"Roboto",sans-serif}
.signup{width:118px;height:38px;background:var(--orange);border:1px solid #fff;color:#fff;font-size:11.5px;font-family:"Roboto",sans-serif;display:flex;align-items:center;justify-content:center}
.foot-line{left:98px;top:2782px;width:1004px;height:1px;background:#888}
.copyright{left:98px;top:2815px;font-family:"Roboto",sans-serif;font-size:13px;color:#eee}
.social{top:2806px;left:906px;display:flex;gap:10px}
.social i{width:32px;height:32px;border:2px solid #fff;border-radius:50%;display:block}
.social i::after{content:"";display:block;width:10px;height:10px;margin:9px auto;border-radius:50%;background:#fff}
</style>
</head>
<body>
<div class="page">

  <!-- header -->
  <div class="abs brand"><span class="brand-dot"></span><span class="brand-name">Sunline Pool Pros</span></div>
  <div class="abs contact-top">
    <span><i class="ico blue"><svg width="14" height="10" viewBox="0 0 14 10"><rect x="0.5" y="0.5" width="13" height="9" fill="none" stroke="#fff"/><path d="M0.5 0.5 7 6 13.5 0.5" fill="none" stroke="#fff"/></svg></i>info@sunlinepoolpros.example</span>
    <span><i class="ico orange"><svg width="14" height="14" viewBox="0 0 14 14"><path d="M3 1l2 3-1.5 1.5c.8 2 2 3.2 4 4L9 8l3 2-1 3C6 13 1 8 1 3z" fill="#fff"/></svg></i>180 555 0147</span>
  </div>
  <nav class="abs nav">
    <a class="current">Home</a><a>About Us</a><a>Services</a><a>Request Quote</a><a>Request Service</a><a>Contact us</a>
  </nav>

  <!-- hero -->
  <section class="abs hero">
    <div class="hero-photo" role="img" aria-label="Photo of a pool skimming net on a pole over rippling blue pool water"></div>
  </section>
  <h1 class="abs hero-title">SUNLINE</h1>
  <p class="abs hero-text">Nemo enim ipsam voluptatem quia voluptas sit asperna tur aut odit aut fugit, sed quia.</p>
  <div class="abs hero-btn">READ MORE</div>
  <svg class="abs arrow" style="left:24px" width="40" height="60" viewBox="0 0 40 60"><path d="M30 4 8 30l22 26" fill="none" stroke="#fff" stroke-width="3"/></svg>
  <svg class="abs arrow" style="right:24px" width="40" height="60" viewBox="0 0 40 60"><path d="M10 4l22 26-22 26" fill="none" stroke="#fff" stroke-width="3"/></svg>
  <svg class="abs hero-wave" viewBox="0 0 1200 80" preserveAspectRatio="none">
    <path d="M0 40 C200 50 420 60 620 56 C820 52 980 10 1200 22 L1200 80 L0 80Z" fill="#fff"/>
    <path d="M0 40 C200 50 420 60 620 56 C820 52 980 10 1200 22" fill="none" stroke="#e8641e" stroke-width="4"/>
  </svg>

  <!-- services -->
  <h2 class="abs sec-title" style="top:716px">OUR SERVICES</h2>
  <div class="abs sec-rule" style="top:771px"></div>

  <div class="abs service" style="left:144px;top:836px">
    <div class="service-icon"><div class="core">
      <svg width="70" height="50" viewBox="0 0 70 50"><path d="M4 32c8-6 14 6 22 0s14 6 22 0 14 6 18 2M4 44c8-6 14 6 22 0s14 6 22 0 14 6 18 2" fill="none" stroke="#fff" stroke-width="4"/><circle cx="52" cy="10" r="6" fill="#fff"/><path d="M14 24 30 10l10 12" fill="none" stroke="#fff" stroke-width="5"/></svg>
    </div></div>
    <h3>POOL CLEANING</h3>
    <p>Nemo enim ipsam voluptatem quia voluptas sit aspernatur aut odit aut fugit, sed quia con sequuntur magni dolores.</p>
    <svg class="swash" width="180" height="16" viewBox="0 0 180 16"><path d="M0 10C50 0 120 0 180 6C120 4 60 6 0 14Z" fill="#2f5f9c"/></svg>
  </div>

  <div class="abs service" style="left:450px;top:836px">
    <div class="service-icon alt"><div class="core">
      <svg width="60" height="70" viewBox="0 0 60 70"><path d="M18 50V14a8 8 0 0 1 16 0M38 50V14a8 8 0 0 1 16 0M18 24h20M18 36h20" fill="none" stroke="#fff" stroke-width="4"/><path d="M4 56c8-5 12 5 20 0s12 5 20 0 10 4 14 1M4 66c8-5 12 5 20 0s12 5 20 0 10 4 14 1" fill="none" stroke="#fff" stroke-width="3.5"/></svg>
    </div></div>
    <h3 class="alt">POOL VACUUMING</h3>
    <p>Nemo enim ipsam voluptatem quia voluptas sit aspernatur aut odit aut fugit, sed quia con sequuntur magni dolores.</p>
    <svg class="swash" width="180" height="16" viewBox="0 0 180 16"><path d="M0 10C50 0 120 0 180 6C120 4 60 6 0 14Z" fill="#2f5f9c"/></svg>
  </div>

  <div class="abs service" style="left:756px;top:836px">
    <div class="service-icon"><div class="core">
      <svg width="66" height="66" viewBox="0 0 66 66"><path d="M8 6 44 44" stroke="#fff" stroke-width="4"/><path d="M44 44l10-4 4 10-10 4z" fill="none" stroke="#fff" stroke-width="3"/><path d="M6 50h54M6 58h54M14 50v10M52 50v10" fill="none" stroke="#fff" stroke-width="3.5"/></svg>
    </div></div>
    <h3>POOL NETTING</h3>
    <p>Nemo enim ipsam voluptatem quia voluptas sit aspernatur aut odit aut fugit, sed quia con sequuntur magni dolores.</p>
    <svg class="swash" width="180" height="16" viewBox="0 0 180 16"><path d="M0 10C50 0 120 0 180 6C120 4 60 6 0 14Z" fill="#2f5f9c"/></svg>
  </div>

  <!-- blog background (sits behind the band) -->
  <div class="abs blog-bg"></div>

  <!-- welcome band -->
  <section class="abs band">
    <svg class="band-bg" viewBox="0 0 1200 570" preserveAspectRatio="none" role="img" aria-label="Faded photo of a pool deck behind a blue overlay">
      <defs><linearGradient id="bandFill" x1="0" y1="0" x2="1" y2="1"><stop offset="0" stop-color="#3f70ac"/><stop offset=".5" stop-color="#5a84b8"/><stop offset="1" stop-color="#2f5f9c"/></linearGradient></defs>
      <path d="M0 20C120 0 260 40 420 30S760 0 900 20 1120 50 1200 10V540C1100 560 960 520 820 540S520 570 360 545 120 520 0 545Z" fill="url(#bandFill)"/>
    </svg>
  </section>
  <div class="abs welcome-photo" role="img" aria-label="Photo of a pool technician cleaning a backyard pool with a net"></div>
  <h2 class="abs welcome-title">WELCOME TO SUNLINE POOL PROS</h2>
  <div class="abs welcome-rule"></div>
  <div class="abs welcome-text">
    <p>Sed ut perspiciatis unde omnis iste natus error sit voluptatem accusantium doloremque lau dan tium, totam rem aperiam, eaque ipsa quae ab illo inventore veritatis et quasi architecto beatae vitae dicta sunt explicabo.</p>
    <p>Nemo enim ipsam voluptatem quia voluptas sit aspernatur aut odit aut fugit, sed quia con sequuntur magni dolores eos qui ratione voluptatem sequi nesciunt. Neque porro quis quam est, qui dolorem ipsum quia dolor sit amet, consectetur.</p>
  </div>
  <div class="abs btn-fill" style="left:532px;top:1610px;width:116px">Read More</div>

  <!-- blog -->
  <h2 class="abs sec-title" style="top:1845px">OUR BLOG POSTS</h2>
  <div class="abs sec-rule" style="top:1900px"></div>

  <article class="abs post" style="left:117px;top:1958px">
    <div class="post-photo" role="img" aria-label="Photo of a pool vacuum head on blue tiles" style="background:linear-gradient(135deg,#3fb0e4,#1f8fd0)"></div>
    <h3 style="color:var(--orange)">Swimming Pool Builders</h3>
    <p>Nemo enim ipsam voluptatem quia voluptas sit aspernatur aut odit aut fugit, sed quia consequun tur magni dolores eos qui ratione.</p>
    <div class="btn solid">Read More</div>
  </article>
  <article class="abs post" style="left:449px;top:1958px">
    <div class="post-photo" role="img" aria-label="Photo of a technician testing pool water at the poolside" style="background:linear-gradient(160deg,#7fa36a,#4aa8d8 60%,#2a86c4)"></div>
    <h3 style="color:var(--blue)">Quality Pool Service</h3>
    <p>Nemo enim ipsam voluptatem quia voluptas sit aspernatur aut odit aut fugit, sed quia consequun tur magni dolores eos qui ratione.</p>
    <div class="btn line">Read More</div>
  </article>
  <article class="abs post" style="left:781px;top:1958px">
    <div class="post-photo" role="img" aria-label="Photo of a worker vacuuming a large commercial pool" style="background:linear-gradient(160deg,#5b6b78,#2f9ad0 50%,#1d7fc0)"></div>
    <h3 style="color:var(--blue)">Commercial Pool Services</h3>
    <p>Nemo enim ipsam voluptatem quia voluptas sit aspernatur aut odit aut fugit, sed quia consequun tur magni dolores eos qui ratione.</p>
    <div class="btn line">Read More</div>
  </article>

  <!-- footer -->
  <svg class="abs footer" viewBox="0 0 1200 466" preserveAspectRatio="none">
    <path d="M0 20C140 50 300 60 460 40S800 0 960 16 1140 40 1200 30V466H0Z" fill="#2f2f2f"/>
  </svg>
  <div class="abs foot-brand"><span class="brand-dot"></span><span class="brand-name" style="font-size:26px">Sunline Pool Pros</span></div>

  <div class="abs foot-h" style="left:375px;top:2500px">QUICK LINKS</div>
  <div class="abs foot-rule" style="left:375px;top:2534px"></div>
  <ul class="abs links" style="left:375px;top:2564px">
    <li>› Home</li><li>› About Us</li><li>› Services</li><li>› Request Quote</li><li>› Request Service</li><li>› Contact us</li>
  </ul>

  <div class="abs foot-h" style="left:570px;top:2500px">CONTACT US</div>
  <div class="abs contact-item" style="left:570px;top:2564px">
    <i class="c-ico"><svg width="12" height="16" viewBox="0 0 12 16"><path d="M6 1a5 5 0 0 1 5 5c0 4-5 9-5 9S1 10 1 6a5 5 0 0 1 5-5z" fill="none" stroke="#fff" stroke-width="1.5"/><circle cx="6" cy="6" r="1.6" fill="#fff"/></svg></i>
    <div><b>ADDRESS,</b><span>45 Harbor Lane AS,<br>2nd Street, UK.</span></div>
  </div>
  <div class="abs contact-item" style="left:570px;top:2642px">
    <i class="c-ico"><svg width="10" height="16" viewBox="0 0 10 16"><rect x="1" y="1" width="8" height="14" rx="1.5" fill="none" stroke="#fff" stroke-width="1.5"/></svg></i>
    <div><b>PHONE:</b><span>180 555 0147</span></div>
  </div>
  <div class="abs contact-item" style="left:570px;top:2702px">
    <i class="c-ico"><svg width="16" height="12" viewBox="0 0 16 12"><rect x="1" y="1" width="14" height="10" fill="#fff"/><path d="M1 1l7 6 7-6" fill="none" stroke="#2f2f2f" stroke-width="1.3"/></svg></i>
    <div><b>Mail:</b><span>info@sunlinepoolpros.example</span></div>
  </div>

  <div class="abs foot-h" style="left:830px;top:2500px">NEWSLETTER SIGNUP</div>
  <div class="abs field" style="left:830px;top:2556px;width:130px">Name</div>
  <div class="abs field" style="left:969px;top:2556px;width:131px">Phone</div>
  <div class="abs field" style="left:830px;top:2600px;width:270px">Email Address</div>
  <div class="abs signup" style="left:830px;top:2654px">SIGNUP NOW</div>

  <div class="abs foot-line"></div>
  <p class="abs copyright">Copyright © 2017 Sunline Pool Pros. All Right Reserved</p>
  <div class="abs social"><i></i><i></i><i></i><i></i><i></i></div>

</div>
</body>
</html>
```